Income Tax Flyer - Updates Needed

Just need to update this flyer design and give it a new look. We would like to keep all the same wording but make it stand out a little more. Our selling point is the "Same Day Tax Advance up to $6,000"

Industry/Entity Type

Lending, Small Loans, Tax Services, Title Loans, Personal Loans

```html
<!DOCTYPE html>
<html lang="en">
<head>
<meta charset="utf-8">
<title>Same Day Tax Advance Flyer</title>
<link rel="stylesheet" href="https://fonts.googleapis.com/css2?family=Poppins:wght@400;500;600;700;800;900&display=swap">
<style>
  :root {
    --page-bg: #e8e7e5;
    --paper: #ffffff;
    --ink-gray: #4a4a4c;
    --brand-red: #c4202b;
    --brand-red-bright: #e12a35;
    --brand-green: #1f6b3a;
    --brand-green-dark: #175a30;
    --text-dark: #2a2a2a;
    --divider: #c9c9c9;
  }
  * { margin: 0; padding: 0; box-sizing: border-box; }
  html, body { width: 1200px; height: 3621px; overflow: hidden; }
  body {
    background: var(--page-bg);
    font-family: "Poppins", sans-serif;
    position: relative;
  }
  .flyer {
    position: absolute;
    left: 100px;
    top: 1103px;
    width: 1000px;
    height: 1414px;
    background: var(--paper);
    overflow: hidden;
    box-shadow: 0 18px 40px rgba(0,0,0,0.12);
  }
  .headline-top {
    position: absolute;
    left: 0; width: 100%;
    top: 36px;
    text-align: center;
    font-weight: 700;
    font-size: 172px;
    line-height: 1;
    letter-spacing: -4px;
    color: var(--ink-gray);
  }
  .headline-bottom {
    position: absolute;
    left: 0; width: 100%;
    top: 186px;
    text-align: center;
    font-weight: 800;
    font-size: 122px;
    line-height: 1;
    letter-spacing: -1px;
    color: var(--brand-red);
  }
  .amount-badge {
    position: absolute;
    left: 251px;
    top: 310px;
    width: 502px;
    height: 92px;
    display: flex;
  }
  .amount-badge .badge-label {
    background: var(--brand-green);
    color: #fff;
    font-weight: 400;
    font-size: 50px;
    width: 205px;
    display: flex; align-items: center; justify-content: center;
    outline: 2px dashed rgba(255,255,255,0.55);
    outline-offset: -7px;
    clip-path: polygon(0 0, 100% 0, 100% 0, 100% 100%, 0 100%);
  }
  .amount-badge .badge-value {
    position: relative;
    flex: 1;
    background: var(--brand-red-bright);
    color: #fff;
    font-weight: 700;
    font-size: 62px;
    display: flex; align-items: center; justify-content: flex-end;
    padding-right: 16px;
    outline: 2px dashed rgba(255,255,255,0.55);
    outline-offset: -7px;
  }
  .amount-badge .badge-value::before {
    content: "";
    position: absolute;
    left: 0; top: 0;
    border-top: 46px solid transparent;
    border-bottom: 46px solid transparent;
    border-left: 34px solid var(--brand-green);
  }
  .photo-area {
    position: absolute;
    left: 537px;
    top: 467px;
    width: 463px;
    height: 720px;
    background: linear-gradient(160deg, #f4efea 0%, #d9c4b3 35%, #9ab4cc 70%, #eef1f4 100%);
    -webkit-mask-image: linear-gradient(to right, transparent 0, #000 90px);
            mask-image: linear-gradient(to right, transparent 0, #000 90px);
  }
  .intro {
    position: absolute;
    left: 43px;
    top: 510px;
    color: var(--brand-green);
    font-weight: 500;
    font-size: 40px;
    line-height: 1.22;
  }
  .intro .intro-highlight {
    display: block;
    margin-top: 4px;
    color: var(--brand-red);
    font-weight: 800;
    font-size: 48px;
  }
  .features {
    position: absolute;
    left: 50px;
    top: 730px;
    width: 450px;
    list-style: none;
  }
  .feature {
    display: flex;
    align-items: center;
    height: 150px;
    border-bottom: 2px dashed var(--divider);
    padding-left: 0;
  }
  .feature:last-child { border-bottom: none; }
  .feature-icon { width: 92px; height: 92px; flex: none; }
  .feature-text {
    margin-left: 42px;
    font-weight: 600;
    font-size: 28px;
    line-height: 1.2;
    color: var(--text-dark);
  }
  .footer-band {
    position: absolute;
    left: 0; bottom: 0;
    width: 1000px; height: 300px;
  }
  .brand-name {
    position: absolute;
    left: 72px;
    top: 1270px;
    width: 300px;
    text-align: center;
    color: #fff;
    font-weight: 500;
    font-size: 30px;
    line-height: 1.2;
  }
  .contact-pill {
    position: absolute;
    left: 491px;
    top: 1216px;
    background: var(--brand-red);
    color: #fff;
    font-weight: 700;
    font-size: 19px;
    padding: 6px 16px;
    border-radius: 6px;
  }
  .contact-line {
    position: absolute;
    left: 491px;
    display: flex; align-items: center;
    color: #fff;
  }
  .contact-line svg { width: 26px; height: 26px; margin-right: 22px; }
  .contact-phone { top: 1276px; font-weight: 700; font-size: 42px; }
  .contact-address { top: 1342px; font-weight: 400; font-size: 28px; letter-spacing: 2px; }
</style>
</head>
<body>
  <article class="flyer">
    <h1 class="headline-top">SAME DAY</h1>
    <h2 class="headline-bottom">TAX ADVANCE</h2>

    <div class="amount-badge">
      <span class="badge-label">UP TO</span>
      <span class="badge-value">$6,000</span>
    </div>

    <div class="photo-area" role="img" aria-label="Photo of a smiling couple reading a document together"></div>

    <p class="intro">File your taxes<br>and apply for an<span class="intro-highlight">Easy Advance!</span></p>

    <ul class="features">
      <li class="feature">
        <svg class="feature-icon" viewBox="0 0 92 92" fill="none" stroke-width="3">
          <rect x="20" y="22" width="62" height="38" rx="3" stroke="#1f6b3a"/>
          <rect x="26" y="28" width="50" height="26" stroke="#1f6b3a"/>
          <circle cx="51" cy="41" r="10" stroke="#c4202b"/>
          <text x="51" y="47" text-anchor="middle" font-size="15" font-weight="700" fill="#c4202b" stroke="none" font-family="Poppins, sans-serif">$</text>
          <circle cx="24" cy="64" r="15" fill="#fff" stroke="#1f6b3a"/>
          <path d="M24 56v8l6 4" stroke="#c4202b"/>
        </svg>
        <span class="feature-text">Available In<br>24 Hours or Less</span>
      </li>
      <li class="feature">
        <svg class="feature-icon" viewBox="0 0 92 92" fill="none" stroke-width="3">
          <circle cx="40" cy="42" r="20" stroke="#1f6b3a" stroke-dasharray="6 5"/>
          <circle cx="40" cy="42" r="12" stroke="#c4202b"/>
          <text x="40" y="48" text-anchor="middle" font-size="15" font-weight="700" fill="#c4202b" stroke="none" font-family="Poppins, sans-serif">$</text>
          <path d="M48 50l6 26 6-9 10 10 5-5-10-10 9-6z" fill="#fff" stroke="#1f6b3a"/>
        </svg>
        <span class="feature-text">Choose Your<br>Loan Amount</span>
      </li>
      <li class="feature">
        <svg class="feature-icon" viewBox="0 0 92 92" fill="none" stroke-width="3">
          <circle cx="56" cy="46" r="24" stroke="#1f6b3a"/>
          <circle cx="56" cy="46" r="16" stroke="#c4202b"/>
          <text x="56" y="54" text-anchor="middle" font-size="22" font-weight="700" fill="#c4202b" stroke="none" font-family="Poppins, sans-serif">$</text>
          <path d="M10 36h18M4 46h22M10 56h18" stroke="#c4202b" stroke-linecap="round"/>
        </svg>
        <span class="feature-text">Quick and Easy</span>
      </li>
    </ul>

    <svg class="footer-band" viewBox="0 0 1000 300" preserveAspectRatio="none">
      <path d="M0 90 Q500 -40 1000 90 L1000 300 L0 300 Z" fill="#c4202b"/>
      <path d="M0 112 Q500 -4 1000 112 L1000 300 L0 300 Z" fill="#ffffff"/>
      <path d="M0 122 Q500 14 1000 122 L1000 300 L0 300 Z" fill="#1f6b3a"/>
    </svg>

    <p class="brand-name">Tallyford<br>Financial Group</p>

    <span class="contact-pill">Contact Us Today!</span>
    <p class="contact-line contact-phone">
      <svg viewBox="0 0 26 26"><rect width="26" height="26" rx="5" fill="#c4202b"/><path d="M8 6c1 0 2 3 2 4s-1 1-1 2 3 5 5 5 1-1 2-1 4 1 4 2-2 3-3 3C11 21 5 15 5 9c0-1 2-3 3-3z" fill="#fff"/></svg>
      Phone Number
    </p>
    <p class="contact-line contact-address">
      <svg viewBox="0 0 26 26"><rect width="26" height="26" rx="5" fill="#c4202b"/><path d="M13 5a6 6 0 0 0-6 6c0 5 6 10 6 10s6-5 6-10a6 6 0 0 0-6-6z" fill="#fff"/><circle cx="13" cy="11" r="2.2" fill="#c4202b"/></svg>
      Address line 1
    </p>
  </article>
</body>
</html>
```